Solo consultant in research/analytics/data science space needs new business card

I need a new business card to promote my solo business as creative problem solver and consultant. I work on business projects for sales and market research and analytics, customer/market insights, and data science. I provide clients data-informed insights and ideas to enhance their businesses. My initial tagline: 'Make your data work for YOU.'

People should hire me because of my diverse background. Because of my Ph.D. in Political Science I have a strong background in research and analytics, project design and management, and communications skills. With my experience as a marketing analyst, a volunteer on non-profit projects, and currently as research consultant I have worked on projects within various industries. I also have a taste for improvisation so I enjoy thinking creatively and appreciate design thinking.

As an introduction to my background: Clients might want to hire me for many types of projects. Clients might wish to understand who their best customers are and how to characterize them. Maybe clients want to know how their customers feel about a certain product or service. Clients might want to know more about their local market area and overall industry. Clients might want to know whether their marketing programs are effective or else what drives their sales revenue. Perhaps clients want to use their data to create something useful for themselves or their customers.

One client hired me to help them decide whether to expand their services to newer customers. I gathered and analyzed information about the local area – the characteristics of people living there as well as the client’s competitors – and described trends and implications. The client was very pleased with the results and submitted them to superiors for approval to move forward.

For another client – who was looking to purchase a house in a metropolitan area – I gathered population and school data about the area. With this, I created an interactive mapping tool so they could zoom in on neighborhoods and learn more about them before they selected a neighborhood to purchase a house. They were happy with the results of my work.

When I worked as a marketing analyst for a consulting firm, a Vice President of Marketing hired us to discover whether or not the company’s marketing programs (i.e. coupons and discounts) were effective. I analyzed their data and our team discovered their marketing was indeed effective. He was very happy and used this to justify their programs to the Finance department (who thought such programs lost revenue).

- Mark Dennis Hollow, Ph.D.

Target Market(s)

Future clients and employers. The most immediate target markets will be other service providers such as consulting companies, marketing firms and ad agencies. I will also use this for meeting with clients in various industries.

Industry/Entity Type

Consulting

Contact Information for Business Card

Since it is my first real business card as a solo practitioner, I want to make an excellent first impression. I want this useful in case someone hires me to work on projects or else hire me to work within a firm or company. The card should convey competence and some creativity while also being neither stuffy nor a data geek.

Colors

Designer to choose colors to be used in the design.

Requirements
Nice to have
• Attached are the starting efforts at the card to add some color. It will be nice to use my name and descriptors on one side and tagline on the other. If anyone has better ideas, I will love to see them!

```html
<!DOCTYPE html>
<html lang="en">
<head>
<meta charset="utf-8">
<title>Mark Dennis Hollow, Ph.D. — Business Card</title>
<link rel="stylesheet" href="https://fonts.googleapis.com/css2?family=Bebas+Neue&family=Roboto:wght@400;700&display=swap">
<style>
  :root {
    --backdrop: #2b2c2e;
    --card: #0a0a0a;
    --ink: #ffffff;
    --ink-soft: #d9d9d9;
    --ink-muted: #a8a8a8;
    --accent: #e0262b;
    --rule: #9a9a9a;
  }
  * { box-sizing: border-box; margin: 0; padding: 0; }
  html, body {
    width: 1200px; height: 900px; overflow: hidden;
    background: var(--backdrop);
  }
  .canvas { position: relative; width: 1200px; height: 900px; }
  .card {
    position: absolute; left: 260px;
    width: 680px; height: 390px;
    background: var(--card);
    border-radius: 28px;
    color: var(--ink);
    box-shadow: 0 18px 40px rgba(0,0,0,0.45);
  }
  .card--identity { top: 40px; }
  .card--tagline { top: 470px; }

  /* Identity side */
  .identity__name {
    position: absolute; left: 48px; top: 42px;
    font-family: "Bebas Neue", sans-serif; font-weight: 400;
    font-size: 40px; letter-spacing: 2.5px; line-height: 1;
  }
  .identity__role {
    position: absolute; left: 48px; top: 128px;
    font-family: "Roboto", sans-serif; font-size: 15px; line-height: 1.35;
  }
  .identity__role strong { display: block; font-weight: 700; color: var(--ink); }
  .identity__role span { display: block; color: var(--ink-muted); }
  .identity__role .identity__handle { display: flex; align-items: center; gap: 8px; }
  .identity__handle i {
    width: 10px; height: 10px; border-radius: 50%;
    background: var(--accent); display: inline-block; flex: none;
  }
  .identity__divider {
    position: absolute; left: 340px; top: 200px;
    width: 2px; height: 90px; background: var(--rule);
  }
  .identity__brand {
    position: absolute; right: 52px; top: 180px;
    display: flex; align-items: center; gap: 10px;
    font-family: "Roboto", sans-serif; font-weight: 700;
    font-size: 26px; line-height: 1; color: var(--ink);
  }
  .identity__brand i {
    width: 14px; height: 14px; background: var(--ink); display: inline-block; flex: none;
  }
  .identity__contact {
    position: absolute; right: 52px; top: 262px;
    text-align: right; font-style: normal;
    font-family: "Roboto", sans-serif; font-size: 16px; line-height: 1.45;
    color: var(--ink-soft);
  }

  /* Tagline side */
  .tagline {
    position: absolute; left: 48px; top: 44px;
    font-family: "Bebas Neue", sans-serif; font-weight: 400;
    font-size: 58px; line-height: 0.92; letter-spacing: 1.5px;
  }
  .services {
    position: absolute; left: 340px; top: 196px;
    list-style: none;
    font-family: "Roboto", sans-serif; font-size: 20px; color: var(--ink-soft);
  }
  .services li { display: flex; align-items: center; gap: 16px; height: 48px; }
  .services svg { width: 30px; height: 30px; flex: none; }
</style>
</head>
<body>
<main class="canvas">

  <section class="card card--identity" aria-label="Card front">
    <h1 class="identity__name">Mark Dennis Hollow, Ph.D.</h1>
    <div class="identity__role">
      <strong>Consultant</strong>
      <span>Lisbon, PT</span>
      <span class="identity__handle"><i></i>@MarkHollow70</span>
    </div>
    <div class="identity__divider"></div>
    <div class="identity__brand"><i></i>Hollow</div>
    <address class="identity__contact">
      +351 912 530 418<br>
      MDHollow70@postbox.com<br>
      MarkDennisHollow.com
    </address>
  </section>

  <section class="card card--tagline" aria-label="Card back">
    <h2 class="tagline">Make<br>Your Data<br>Work<br>For You</h2>
    <ul class="services">
      <li>
        <svg viewBox="0 0 30 30" fill="none" stroke="var(--accent)" stroke-width="2">
          <rect x="3" y="4" width="24" height="17" rx="1"/>
          <path d="M11 26h8M15 21v5"/>
          <path d="M10 17v-4M15 17v-8M20 17v-6" stroke-width="2.4"/>
        </svg>
        Research/Analytics
      </li>
      <li>
        <svg viewBox="0 0 30 30" fill="none" stroke="var(--accent)" stroke-width="2">
          <path d="M7 19a8 8 0 0 1 16 0z" fill="var(--accent)"/>
          <path d="M4 22h22M7 25h16"/>
          <path d="M15 4v4M6 8l2.5 2.5M24 8l-2.5 2.5M2.5 15h3M24.5 15h3"/>
        </svg>
        Customer Intelligence
      </li>
      <li>
        <svg viewBox="0 0 30 30" fill="none" stroke="var(--accent)" stroke-width="2">
          <path d="M6 3h13l5 5v19H6z"/>
          <path d="M19 3v5h5"/>
          <path d="M10 14h10M10 18h10M10 22h7"/>
        </svg>
        Data Science
      </li>
    </ul>
  </section>

</main>
</body>
</html>
```